Flyer for an IT consultancy firm

Design guidelines

We are an IT consultancy firm based in Iceland. We have a website at: www.vorlatek.com where you can get acquainted with our activities.
We require a double-sided flyer in A4 format to be handed out in conferences, trade shows etc. The flyer is basically a summarized overview of our range of services.

The deliverable should incorporate some visual elements that are relevant to our line of business such as:
• computers
• cybersecurity
• networks
Also, it would be nice to have visuals relating to Icelandic geography, to further emphasize our local roots. Some suggested keywords:
• volcano
• aurora borealis
• waterfall
• glacier

NB: the flyer will be printed out, therefore image resolution needs to be high enough to render nicely on paper.
The primary colors would be red, black and white – in line with our logo. But there is freedom to diverge and go for a different color scheme.

The logo should be present on the top front of the flyer. The URL www.vorlatek.com needs to be mentioned prominently, for example at the bottom of the page.

Examples of design we like:
• https://www.plimora.com/design/58130946
• https://www.plimora.com/design/58173352

Attached:
• the text for the brochure in PDF format
• our logo in vector format

Industry/Entity Type

IT, software, cybersecurity

Colors
EB3D1F
EC4F4E
F09395
F8D3D4
FCEDEE

Requirements
Must have
• existing logo, and visuals related to computer, networks etc
Nice to have
• Icelandic geography/landscapes

```html
<!DOCTYPE html>
<html lang="en">
<head>
<meta charset="utf-8">
<title>Vorlatek ehf – IT Consultancy Flyer</title>
<link href="https://fonts.googleapis.com/css2?family=Manrope:wght@600;700&family=Roboto:wght@400&display=swap" rel="stylesheet">
<style>
:root{
  --stage:#8e8e8e;
  --paper:#ffffff;
  --red:#8b0000;
  --red-bright:#a30d0d;
  --red-deep:#5a0606;
  --ink:#111111;
  --text:#2a2a2a;
  --muted-grey:#e6e6e8;
}
*{margin:0;padding:0;box-sizing:border-box}
html,body{width:1200px;height:802px;overflow:hidden;background:var(--stage)}
.stage{position:relative;width:1200px;height:802px}
.page{position:absolute;top:68px;width:515px;height:666px;background:var(--paper);overflow:hidden;box-shadow:0 4px 14px rgba(0,0,0,.35);font-family:"Roboto",sans-serif;color:var(--text)}
.page--front{left:61px}
.page--back{left:624px}
.hero-art{position:absolute;left:0;top:0;width:515px;height:330px}
.brand{position:absolute;top:9px;display:flex;align-items:center;gap:6px}
.brand__dot{width:24px;height:24px;border-radius:50%;background:var(--red)}
.brand__name{font-family:"Manrope",sans-serif;font-weight:700;font-size:15px;letter-spacing:.5px;color:var(--ink)}
.page--front .brand{left:366px}
.page--back .brand{left:31px}
.hero-title{position:absolute;top:84px;font-family:"Manrope",sans-serif;font-weight:700;font-size:15.3px;line-height:19px;color:#fff;text-transform:uppercase}
.hero-text{position:absolute;top:152px;font-size:7.9px;line-height:12.5px;color:#fff}
.page--front .hero-title,.page--front .hero-text{left:289px}
.page--front .hero-text{width:202px}
.page--back .hero-title,.page--back .hero-text{left:31px}
.page--back .hero-text{width:188px}
.landscape{position:absolute;left:0;bottom:26px;width:100%;height:150px;background:linear-gradient(180deg,rgba(255,255,255,0) 0%,var(--muted-grey) 55%,#d9d9dc 100%)}
.service{position:absolute;width:222px}
.service__icon{position:absolute;left:0;top:0;width:39px;height:39px;border-radius:50%;background:#fff;box-shadow:0 1px 5px rgba(0,0,0,.22);display:flex;align-items:center;justify-content:center}
.service__title{position:absolute;left:50px;top:0;height:39px;display:flex;align-items:center;font-family:"Manrope",sans-serif;font-weight:700;font-size:9.8px;line-height:12.5px;color:var(--ink);text-transform:uppercase}
.service__text{position:absolute;left:0;top:50px;width:222px;font-size:7.4px;line-height:11.7px;text-align:justify}
.service--dev{left:30px;top:344px}
.service--sys{left:265px;top:344px}
.service--mon{left:30px;top:478px}
.service--auto{left:265px;top:478px}
.security-photo{position:absolute;left:31px;top:334px;width:211px;height:200px;border-radius:7px;background:linear-gradient(120deg,#c9d2de 0%,#6b7f9e 45%,#1e2533 100%)}
.security{position:absolute;left:265px;top:354px;width:221px}
.security__title{font-family:"Manrope",sans-serif;font-weight:700;font-size:14.3px;color:var(--ink);text-transform:uppercase;margin-bottom:11px}
.security p{font-size:7.4px;line-height:11.7px;text-align:justify;margin-bottom:6px}
.cta{position:absolute;left:0;top:558px;width:100%;text-align:center}
.cta__line{font-family:"Manrope",sans-serif;font-weight:700;font-size:14.3px;line-height:21px;color:var(--ink)}
.cta__name{font-family:"Roboto",sans-serif;font-size:12.3px;color:var(--red-bright);margin-top:4px}
.footer{position:absolute;left:0;bottom:0;width:100%;height:29px;background:var(--ink);border-top:3px solid var(--red-bright);display:flex;align-items:center;justify-content:center;gap:17px}
.contact{display:flex;align-items:center;gap:6px;font-size:7.7px;color:#fff}
.contact__icon{width:13px;height:13px;border-radius:50%;background:#fff;display:flex;align-items:center;justify-content:center}
</style>
</head>
<body>
<div class="stage">

  <section class="page page--front">
    <svg class="hero-art" viewBox="0 0 515 330">
      <defs>
        <linearGradient id="bandFront" x1="0" y1="0" x2="0" y2="1">
          <stop offset="0" stop-color="#8b0000"/><stop offset=".6" stop-color="#6a0303"/><stop offset="1" stop-color="#140404"/>
        </linearGradient>
        <linearGradient id="ringFront" x1="0" y1="0" x2="0" y2="1">
          <stop offset="0" stop-color="#8b0000"/><stop offset="1" stop-color="#0a0a0a"/>
        </linearGradient>
        <radialGradient id="photoFront" cx=".6" cy=".4" r=".8">
          <stop offset="0" stop-color="#9a9a9a"/><stop offset=".6" stop-color="#4a4a4a"/><stop offset="1" stop-color="#151515"/>
        </radialGradient>
      </defs>
      <rect x="205" y="46" width="310" height="234" fill="url(#bandFront)"/>
      <circle cx="101" cy="163" r="146" fill="#fff"/>
      <circle cx="101" cy="163" r="146" fill="none" stroke="url(#ringFront)" stroke-width="4.5"/>
      <line x1="254" y1="136" x2="338" y2="136" stroke="#fff" stroke-width="1"/>
      <circle cx="338" cy="136" r="4" fill="#fff"/>
      <circle cx="101" cy="163" r="133" fill="url(#photoFront)" role="img" aria-label="Black and white photo of hands typing on a keyboard with a cybersecurity shield overlay"/>
    </svg>

    <div class="brand"><span class="brand__dot"></span><span class="brand__name">VORLATEK</span></div>
    <h1 class="hero-title">Vorlatek ehf – Your<br>Icelandic IT Partner</h1>
    <p class="hero-text">Step into a world of comprehensive IT solutions tailored to your unique needs. Our services, available on a contract or as-needed basis, are designed to empower your business and equip you with the tools you need to succeed. More than just a list of offerings, they’re a commitment to quality, a dedication to innovation, and a promise of reliability.</p>

    <div class="landscape" role="img" aria-label="Faint grey glacier and mountain landscape"></div>

    <article class="service service--dev">
      <div class="service__icon"><svg width="22" height="22" viewBox="0 0 22 22"><circle cx="11" cy="11" r="8" fill="none" stroke="#a30d0d" stroke-width="3" stroke-dasharray="3 2"/><circle cx="11" cy="11" r="5.5" fill="#a30d0d"/><path d="M9 9l-2 2 2 2M13 9l2 2-2 2" fill="none" stroke="#fff" stroke-width="1"/></svg></div>
      <h2 class="service__title">Software Development<br>and Integration Services</h2>
      <p class="service__text">We specialize in custom software development across different platforms (desktop, server, embedded systems). We are open source software advocates, and leverage decades of experience to deliver innovative and cost-effective solutions tailored to your needs. Let’s build the perfect software solution for you.</p>
    </article>

    <article class="service service--sys">
      <div class="service__icon"><svg width="22" height="22" viewBox="0 0 22 22"><circle cx="9" cy="9" r="5.5" fill="none" stroke="#a30d0d" stroke-width="3" stroke-dasharray="2.5 1.5"/><path d="M6.5 9l2 2 3-3.5" fill="none" stroke="#a30d0d" stroke-width="1.4"/><circle cx="16" cy="16" r="3.5" fill="none" stroke="#a30d0d" stroke-width="2.4" stroke-dasharray="2 1.3"/></svg></div>
      <h2 class="service__title">Systems<br>Administration</h2>
      <p class="service__text">Are you having trouble with your IT infrastructure and in need of qualified personnel to take care of them? Or do you simply need a watchful and expert eye to ensure your systems keep running smoothly? We provide on-site and remote sysadmin services to manage your systems and bring you peace of mind. Take back control.</p>
    </article>

    <article class="service service--mon">
      <div class="service__icon"><svg width="22" height="22" viewBox="0 0 22 22"><rect x="4" y="8" width="3" height="6" fill="#a30d0d"/><rect x="8.5" y="5" width="3" height="9" fill="#a30d0d"/><rect x="13" y="7" width="3" height="7" fill="#a30d0d"/><rect x="2" y="14" width="18" height="2" fill="#a30d0d"/><path d="M5 17a7 4 0 0 0 12 0" fill="none" stroke="#a30d0d" stroke-width="1.5"/></svg></div>
      <h2 class="service__title">Infrastructure<br>Monitoring Services</h2>
      <p class="service__text">Do you know what is really going on inside your systems? We leverage leading open source monitoring solutions to bring visibility to your infrastructure. Monitor your systems proactively to ensure that they remain healthy at all times. Collect logs in real time and be notified when problems occur or warnings are raised. Fix issues before they become problems.</p>
    </article>

    <article class="service service--auto">
      <div class="service__icon"><svg width="22" height="22" viewBox="0 0 22 22"><circle cx="11" cy="11" r="8.5" fill="none" stroke="#a30d0d" stroke-width="1" stroke-dasharray="10 3"/><circle cx="11" cy="11" r="5" fill="none" stroke="#a30d0d" stroke-width="3" stroke-dasharray="2.2 1.4"/><circle cx="11" cy="11" r="2" fill="#a30d0d"/></svg></div>
      <h2 class="service__title">Automation</h2>
      <p class="service__text">Because you need effective tools to grow and prosper, it is essential that your IT systems align with your operational needs. We offer a comprehensive review of your business and IT environment so as to optimize the means already at your disposal. We streamline your workflow and develop new tools as needed, to make your IT systems work harder for you. Let us automate the boring stuff for you.</p>
    </article>

    <footer class="footer">
      <span class="contact"><span class="contact__icon"><svg width="7" height="7" viewBox="0 0 10 10"><path d="M2 1l2 2-1 1.5a6 6 0 0 0 2.5 2.5L7 6l2 2-1.5 1.5C4 9 1 6 .5 2.5z" fill="#a30d0d"/></svg></span>+354 555 0192</span>
      <span class="contact"><span class="contact__icon"><svg width="7" height="6" viewBox="0 0 10 8"><rect x="0" y="0" width="10" height="8" rx="1" fill="#a30d0d"/><path d="M0 1l5 3.5L10 1" fill="none" stroke="#fff" stroke-width="1"/></svg></span>info@vorlatek.com</span>
      <span class="contact"><span class="contact__icon"><svg width="7" height="7" viewBox="0 0 10 10"><circle cx="5" cy="5" r="4.5" fill="#a30d0d"/><path d="M.5 5h9M5 .5v9" stroke="#fff" stroke-width=".7"/></svg></span>www.vorlatek.com</span>
    </footer>
  </section>

  <section class="page page--back">
    <svg class="hero-art" viewBox="0 0 515 330">
      <defs>
        <linearGradient id="bandBack" x1="0" y1="0" x2="0" y2="1">
          <stop offset="0" stop-color="#8b0000"/><stop offset=".6" stop-color="#6a0303"/><stop offset="1" stop-color="#140404"/>
        </linearGradient>
        <linearGradient id="ringBack" x1="0" y1="0" x2="0" y2="1">
          <stop offset="0" stop-color="#8b0000"/><stop offset="1" stop-color="#0a0a0a"/>
        </linearGradient>
        <radialGradient id="photoBack" cx=".45" cy=".45" r=".8">
          <stop offset="0" stop-color="#a8a8a8"/><stop offset=".55" stop-color="#505050"/><stop offset="1" stop-color="#141414"/>
        </radialGradient>
      </defs>
      <rect x="0" y="46" width="310" height="234" fill="url(#bandBack)"/>
      <circle cx="415" cy="163" r="146" fill="#fff"/>
      <circle cx="415" cy="163" r="146" fill="none" stroke="url(#ringBack)" stroke-width="4.5"/>
      <line x1="0" y1="136" x2="79" y2="136" stroke="#fff" stroke-width="1"/>
      <circle cx="79" cy="136" r="4" fill="#fff"/>
      <circle cx="415" cy="163" r="133" fill="url(#photoBack)" role="img" aria-label="Black and white photo of a laptop keyboard with a glowing network of security icons"/>
    </svg>

    <div class="brand"><span class="brand__dot"></span><span class="brand__name">VORLATEK</span></div>
    <h2 class="hero-title">Technology<br>Assessment Services</h2>
    <p class="hero-text">Unsure about which tools are right for you or what IT strategy to pursue to help your business grow? We conduct market research and perform technical evaluations of software and hardware products to determine the best solutions for your company. Let’s empower your business with leading-edge solutions.</p>

    <div class="landscape" role="img" aria-label="Faint grey glacier and mountain landscape"></div>

    <div class="security-photo" role="img" aria-label="Photo of an IT engineer working on a laptop in a server room"></div>
    <article class="security">
      <h2 class="security__title">Security Services</h2>
      <p>We understand the importance of security in today’s digital landscape. That’s why we offer comprehensive security services, including network audits to find and remedy flaws before they can be exploited to your disadvantage.</p>
      <p>We perform a thorough review of your IT environment to identify and remediate the weak spots, in order to keep your business secure, protect your assets and your reputation. Let’s raise your security posture to the highest standards, so that you don't become the next victim - or headline.</p>
      <p>Bring the good guys in to keep the bad guys out.</p>
    </article>

    <div class="cta">
      <p class="cta__line">Get in touch with us today to discuss your<br>IT needs in strict confidence.</p>
      <p class="cta__name">Vorlatek ehf</p>
    </div>

    <footer class="footer">
      <span class="contact"><span class="contact__icon"><svg width="7" height="7" viewBox="0 0 10 10"><path d="M2 1l2 2-1 1.5a6 6 0 0 0 2.5 2.5L7 6l2 2-1.5 1.5C4 9 1 6 .5 2.5z" fill="#a30d0d"/></svg></span>+354 555 0192</span>
      <span class="contact"><span class="contact__icon"><svg width="7" height="6" viewBox="0 0 10 8"><rect x="0" y="0" width="10" height="8" rx="1" fill="#a30d0d"/><path d="M0 1l5 3.5L10 1" fill="none" stroke="#fff" stroke-width="1"/></svg></span>info@vorlatek.com</span>
      <span class="contact"><span class="contact__icon"><svg width="7" height="7" viewBox="0 0 10 10"><circle cx="5" cy="5" r="4.5" fill="#a30d0d"/><path d="M.5 5h9M5 .5v9" stroke="#fff" stroke-width=".7"/></svg></span>www.vorlatek.com</span>
    </footer>
  </section>

</div>
</body>
</html>
```